Business Card Design

Name of company: Brisk Property Maintenance.
We are a new start up business.
The company is involved in general property maintenance around residential properties and high rise apartment buildings.
We carry out all types of property maintenance such as:
*Handyman work
*Plumbing
*Painting
*Electrical
*Window cleaning
*Gardens / Landscaping

Target Market(s)

*Real Estate Agents
*Body corporate managers
*Private apartment owners

Industry/Entity Type

Property Maintenance

Requirements
Must have
• Name: Dean Malloy
Address: PO Box 3862
Carrow Hill Crossing
VIC 3915
Phone: 0431 962 305
Email: dean@briskpropertymaintenance
Website: www.briskpropertymaintenance.example.au
Nice to have
• We don't have any corporate logo so you can design what you think is appropriate

```html
<!DOCTYPE html>
<html lang="en">
<head>
<meta charset="utf-8">
<title>Brisk Property Maintenance – Business Card</title>
<link rel="stylesheet" href="https://fonts.googleapis.com/css2?family=Arimo:wght@400;700&display=swap">
<style>
  :root {
    --page-bg: #c4e2f3;
    --card-blue-light: #2f8fd6;
    --card-blue: #1a6fbf;
    --card-blue-dark: #0f4f99;
    --band-white: #f2f4f6;
    --name-orange: #e0861c;
    --brand-blue: #1a62ad;
    --text-white: #ffffff;
  }
  * { margin: 0; padding: 0; box-sizing: border-box; }
  html, body {
    width: 1200px; height: 955px; overflow: hidden;
    background: var(--page-bg);
    font-family: "Arimo", Arial, sans-serif;
  }
  .canvas {
    width: 1200px; height: 955px;
    display: flex; align-items: center; justify-content: center;
  }
  .business-card {
    position: relative;
    width: 840px; height: 480px;
    border-radius: 6px;
    overflow: hidden;
    background: radial-gradient(ellipse at 70% 30%, var(--card-blue-light), var(--card-blue) 55%, var(--card-blue-dark));
    box-shadow: 0 10px 30px rgba(20, 60, 100, 0.25);
  }
  .name-band {
    position: absolute; left: 0; top: 0;
    width: 840px; height: 200px;
  }
  .holder-name {
    position: absolute; left: 56px; top: 118px;
    font-size: 44px; font-weight: 700;
    font-variant: small-caps;
    color: var(--name-orange);
    letter-spacing: 1px;
  }
  .brand {
    position: absolute; right: 48px; top: 48px;
    display: flex; align-items: center; gap: 14px;
  }
  .brand-dot {
    width: 44px; height: 44px; border-radius: 50%;
    background: var(--brand-blue);
  }
  .brand-name {
    font-size: 20px; font-weight: 700;
    color: var(--brand-blue);
    text-transform: uppercase;
    letter-spacing: 1.5px;
  }
  .contact-list {
    position: absolute; left: 56px; top: 222px;
    list-style: none;
    color: var(--text-white);
    font-size: 23px; line-height: 1.3;
  }
  .contact-item {
    display: flex; align-items: flex-start; gap: 14px;
    margin-bottom: 10px;
  }
  .contact-icon {
    flex: none; width: 28px; height: 28px; margin-top: 1px;
  }
</style>
</head>
<body>
<main class="canvas">
  <article class="business-card">
    <svg class="name-band" viewBox="0 0 840 200" aria-hidden="true">
      <polygon points="0,70 840,22 840,158 0,200" fill="var(--band-white)"/>
    </svg>
    <h1 class="holder-name">Dean Malloy</h1>
    <div class="brand">
      <span class="brand-dot"></span>
      <span class="brand-name">Brisk Property Maintenance</span>
    </div>
    <ul class="contact-list">
      <li class="contact-item">
        <svg class="contact-icon" viewBox="0 0 28 28" aria-hidden="true">
          <circle cx="14" cy="14" r="13" fill="#fff"/>
          <path d="M14 6a5 5 0 0 0-5 5c0 4 5 10 5 10s5-6 5-10a5 5 0 0 0-5-5z" fill="var(--card-blue)"/>
          <circle cx="14" cy="11" r="1.8" fill="#fff"/>
        </svg>
        <span>PO Box 3862<br>Carrow Hill Crossing<br>VIC 3915</span>
      </li>
      <li class="contact-item">
        <svg class="contact-icon" viewBox="0 0 28 28" aria-hidden="true">
          <circle cx="14" cy="14" r="13" fill="#fff"/>
          <rect x="7" y="9" width="14" height="10" rx="1" fill="var(--card-blue)"/>
          <path d="M7.5 9.5 14 15l6.5-5.5" stroke="#fff" stroke-width="1.4" fill="none"/>
        </svg>
        <span>dean@briskpropertymaintenance</span>
      </li>
      <li class="contact-item">
        <svg class="contact-icon" viewBox="0 0 28 28" aria-hidden="true">
          <circle cx="14" cy="14" r="13" fill="#fff"/>
          <path d="M10 7l3 3-2 2c1 2 3 4 5 5l2-2 3 3-2 3c-5 0-11-6-11-11z" fill="var(--card-blue)"/>
        </svg>
        <span>0431 962 305</span>
      </li>
      <li class="contact-item">
        <svg class="contact-icon" viewBox="0 0 28 28" aria-hidden="true">
          <circle cx="14" cy="14" r="13" fill="#fff"/>
          <g stroke="var(--card-blue)" stroke-width="1.5" fill="none">
            <circle cx="14" cy="14" r="7"/>
            <ellipse cx="14" cy="14" rx="3" ry="7"/>
            <line x1="7" y1="14" x2="21" y2="14"/>
          </g>
        </svg>
        <span>www.briskpropertymaintenance.example.au</span>
      </li>
    </ul>
  </article>
</main>
</body>
</html>
```